BrivoMatex. Lantern for the Steady Growth. Business card

Professional business card for BrivoMatex (Lantern for the Steady Growth)
My rationale: Strategy-> Execution-> Results-> Value that lead to the BrivoMatex name: We put the Lantern for the Steady Growth.
We deliver value to our customers helping them at defining a good strategy (cyan arrow). 90% of well formulated strategies fail due to poor execution so we also consider strategical execution very important (green arrow). Due to the execution we obtain the results (blue arrow). Finally, the results provide feedback to redefine strategy, and the new strategy has to be executed and new results obtained providing new feedback and on and on. It's like a wheel that finally, must create corporate value: value for shareholders, staholders, employees, providers...-

Target Market(s)

CEOs and steering comitees , invewrnent funds

Industry/Entity Type

Business Consultant

Contact Information for Business Card

Tommaso Ferlini
CEO & Founder
tommaso.ferlini@brivomatex.example
Mobile: +34 611.205.938
www.brivomatex.example

Colors

Designer to choose colors to be used in the design.

Requirements
Nice to have
• Nice to hace the words: Strategy, execution, results
• Nice to vave the claim: Lantern for the Steady Growth
• The three colors should be shown:
• cyan for STRATEGY
• green for EXECUTION
• blue for RESULTS
Should not have
• Complete black background

```html
<!DOCTYPE html>
<html lang="en">
<head>
<meta charset="utf-8">
<title>BrivoMatex – Business Card</title>
<link rel="stylesheet" href="https://fonts.googleapis.com/css2?family=Source+Sans+3:wght@400;600;700&display=swap">
<style>
  :root {
    --backdrop: #939598;
    --card-white: #ffffff;
    --brand-blue: #253c8f;
    --strategy-cyan: #2ea7e0;
    --execution-green: #8dc63f;
    --text-on-blue: #ffffff;
  }
  * { margin: 0; padding: 0; box-sizing: border-box; }
  html, body {
    width: 1200px;
    height: 1000px;
    overflow: hidden;
    background: var(--backdrop);
    font-family: "Source Sans 3", "Myriad Pro", Arial, sans-serif;
  }
  .business-card {
    position: absolute;
    left: 133px;
    top: 233px;
    width: 934px;
    height: 534px;
    background: var(--card-white);
    overflow: hidden;
  }
  .card-sweep {
    position: absolute;
    inset: 0;
    width: 934px;
    height: 534px;
  }
  .card-sweep path { fill: var(--brand-blue); }

  .brand-name {
    position: absolute;
    left: 70px;
    top: 178px;
    font-size: 52px;
    font-weight: 600;
    letter-spacing: -1px;
    color: var(--brand-blue);
    line-height: 1;
  }
  .pillars {
    position: absolute;
    left: 72px;
    top: 298px;
    list-style: none;
    font-size: 26px;
    font-weight: 700;
    line-height: 44px;
    letter-spacing: 0.2px;
  }
  .pillar-strategy { color: var(--strategy-cyan); }
  .pillar-execution { color: var(--execution-green); }
  .pillar-results { color: var(--brand-blue); }

  .person {
    position: absolute;
    left: 383px;
    top: 116px;
    color: var(--text-on-blue);
  }
  .person-name {
    font-size: 33px;
    font-weight: 700;
    line-height: 1.1;
    letter-spacing: 0.3px;
  }
  .person-role {
    font-size: 25px;
    font-weight: 400;
    margin-top: 6px;
  }

  .contact-list {
    position: absolute;
    left: 379px;
    top: 296px;
    list-style: none;
    color: var(--text-on-blue);
    font-size: 27px;
    line-height: 44px;
  }
  .contact-item {
    display: flex;
    align-items: center;
    gap: 14px;
  }
  .contact-icon {
    width: 34px;
    height: 34px;
    flex: none;
  }
  .contact-icon * { fill: none; stroke: var(--text-on-blue); }
</style>
</head>
<body>
  <div class="business-card">
    <svg class="card-sweep" viewBox="0 0 934 534" aria-hidden="true">
      <path d="M369 0 C350 210 280 420 130 534 L934 534 L934 0 Z"/>
    </svg>

    <div class="brand-name">BrivoMatex</div>

    <ul class="pillars">
      <li class="pillar-strategy">STRATEGY</li>
      <li class="pillar-execution">EXECUTION</li>
      <li class="pillar-results">RESULTS</li>
    </ul>

    <div class="person">
      <div class="person-name">Tommaso Ferlini</div>
      <div class="person-role">CEO &amp; Founder</div>
    </div>

    <ul class="contact-list">
      <li class="contact-item">
        <svg class="contact-icon" viewBox="0 0 34 34" aria-hidden="true">
          <rect x="2" y="8" width="30" height="19" style="fill:#fff;stroke:none"/>
          <path d="M2 8 L17 20 L32 8" style="stroke:#253c8f;stroke-width:2.2"/>
          <path d="M2 27 L13 17 M32 27 L21 17" style="stroke:#253c8f;stroke-width:2"/>
        </svg>
        <span>tommaso.ferlini@brivomatex.example</span>
      </li>
      <li class="contact-item">
        <svg class="contact-icon" viewBox="0 0 34 34" aria-hidden="true">
          <rect x="8" y="2" width="18" height="30" rx="2" style="fill:#fff;stroke:none"/>
          <rect x="11" y="6" width="12" height="21" style="fill:#253c8f;stroke:none"/>
        </svg>
        <span>+34 611.205.938</span>
      </li>
      <li class="contact-item">
        <svg class="contact-icon" viewBox="0 0 34 34" aria-hidden="true">
          <circle cx="17" cy="17" r="15" style="fill:#fff;stroke:none"/>
          <g style="stroke:#253c8f;stroke-width:1.6;fill:none">
            <ellipse cx="17" cy="17" rx="6" ry="15"/>
            <line x1="17" y1="2" x2="17" y2="32"/>
            <line x1="2" y1="17" x2="32" y2="17"/>
            <path d="M5 9.5 H29 M5 24.5 H29"/>
          </g>
        </svg>
        <span>www.brivomatex.example</span>
      </li>
    </ul>
  </div>
</body>
</html>
```